pennworths top finds

i want a creative logo,and a webpage that looks like a e-commerce with a inner city,or a rural background, or anything that makes you notice the page,there is no limit to the creativity,it would have 8 categories,jewlry=3pgs,beauty=3pgs,kids baby-toy=2pgs,shirts=2pgs,shoes=2pgs,gaming=2pgs,watches=2pgs. all credit cards plus coinlet acceptable,17 page total,the last page for secure billing.if there are any questions im here for you.

Reason: so everyone has a chance to submit results

Target Market(s)

my target market is people that just might find something they like for a reasonable price

Industry/Entity Type

E-Commerce

Requirements
Must have
• payment options are a must,they set the table for everything
Nice to have
• items mentioned above plus creativity

```html
<!DOCTYPE html>
<html lang="en">
<head>
<meta charset="utf-8">
<title>Pennworths Top Finds</title>
<link href="https://fonts.googleapis.com/css2?family=Arimo:wght@400;700&family=Oswald:wght@300;400&family=Yellowtail&display=swap" rel="stylesheet">
<style>
:root{
  --page:#1b1b1b;
  --column:#0d0d0d;
  --blue:#2f86e6;
  --blue-dark:#1c62c4;
  --panel:#e9e9e9;
  --red:#c8141b;
  --yellow:#ffe100;
  --orange:#f7a21b;
  --price:#1d8fe0;
  --text:#111;
  --white:#fff;
  --btn:#2c2c2c;
}
*{box-sizing:border-box;margin:0;padding:0}
html,body{width:853px;height:1200px;overflow:hidden}
body{background:var(--page);font-family:"Arimo",Arial,sans-serif;color:var(--text);position:relative}
.page{position:absolute;left:32px;top:0;width:789px;height:1200px;background:var(--column)}
.abs{position:absolute}

/* header */
.topbar{left:49px;top:7px;width:754px;height:53px;background:linear-gradient(#5aa6f2,var(--blue) 55%,var(--blue-dark));border-radius:3px}
.brand{left:80px;top:16px;color:var(--white);font-weight:700;font-size:19px;letter-spacing:.5px;text-transform:uppercase;display:flex;align-items:center;gap:8px}
.brand-mark{width:14px;height:14px;background:var(--white)}
.topnav{right:62px;top:26px;color:var(--white);font-size:11px;font-weight:700}

/* search */
.searchbar{left:67px;top:83px;width:488px;height:53px;background:linear-gradient(#f4f4f4,#cfcfcf);border-radius:3px}
.search-label{left:78px;top:97px;font-size:18px;font-weight:700}
.select{left:148px;top:97px;width:166px;height:22px;background:var(--white);border:1px solid #999;font-size:11px;padding:4px 6px}
.select::after{content:"";position:absolute;right:2px;top:2px;width:14px;height:16px;background:#d8d8e8;border:1px solid #888}
.keyword{left:324px;top:97px;width:170px;height:22px;background:var(--white);border:1px solid #999;font-size:11px;padding:4px 8px;color:#333}
.go{left:502px;top:97px;width:24px;height:24px;border-radius:50%;background:var(--orange);color:var(--white);font-size:12px;font-weight:700;text-align:center;line-height:24px}
.account{left:575px;top:93px;width:210px;text-align:right;color:var(--white);font-size:12px;line-height:18px}
.account .hl{color:var(--yellow)}

/* banners */
.promo-black{left:67px;top:153px;width:353px;height:27px;background:#000;border:1px solid #444;color:var(--white);font-size:17px;padding:4px 8px;letter-spacing:.5px}
.promo-black b{font-weight:700}
.promo-black .preview{position:absolute;right:8px;top:8px;font-size:9px;color:var(--red);font-weight:700;letter-spacing:0}
.promo-bag{left:424px;top:153px;width:359px;height:27px;background:#fff;border:1px solid #9b2fa0}
.promo-bag .title{position:absolute;left:10px;top:1px;color:#8d1f8f;font-weight:700;font-size:15px}
.promo-bag .sub{position:absolute;left:10px;top:16px;color:var(--red);font-size:8px;font-weight:700}
.promo-bag .goods{position:absolute;right:2px;top:2px;width:164px;height:21px;background:linear-gradient(90deg,#6aa86a,#d9d2a0,#e0b040,#a1c660)}

/* sidebar */
.newbox{left:67px;top:195px;width:156px;height:38px;background:#000;border:1px solid #555;color:var(--yellow);font-size:11px;font-weight:700;text-align:center;line-height:15px;padding-top:4px}
.newbox span{color:var(--white);letter-spacing:3px}
.tabs{left:67px;top:240px;width:156px;height:17px;display:flex;font-size:10px;font-weight:700}
.tab{flex:1;text-align:center;line-height:17px;background:var(--white)}
.tab.active{background:var(--yellow);color:var(--red)}
.cats{left:72px;top:261px;width:151px;list-style:none}
.cats li{height:23.7px;line-height:22px;font-size:9px;font-weight:700;padding-left:16px;background:linear-gradient(90deg,#fafafa,#d8d8d8);border-bottom:1.7px solid #999}
.shipbox{left:67px;top:703px;width:156px;height:60px;background:linear-gradient(#555,#2a2a2a);color:var(--yellow);font-size:13px;font-weight:700;line-height:18px;padding:4px 7px}
.shipbox .w{color:var(--white)}
.shipbox .b{color:#39b0ff}
.eurobox{left:67px;top:777px;width:156px;height:67px;background:linear-gradient(120deg,#1e66c6,#0b3c8e);color:var(--white);font-weight:700;font-size:11px;line-height:12px;padding:8px 9px}
.eurobox .amt{font-size:26px;line-height:28px;color:var(--yellow)}
.eurobox .amt small{font-size:15px;color:var(--white)}
.social{left:67px;top:860px;width:156px;height:67px;background:#f1f1f1;border-radius:4px;padding:7px 10px}
.social h4{font-size:11px}
.social-row{display:flex;gap:4px;margin-top:8px}
.chip{font-size:7.5px;font-weight:700;color:var(--white);background:#3a66a8;padding:5px 2px;border-radius:2px}
.cards{left:73px;top:951px;display:flex;gap:4px}
.card{width:35px;height:22px;background:var(--white);border:1px solid #888;font-size:7px;font-weight:700;text-align:center;line-height:20px;color:#222}

/* hero */
.hero{left:223px;top:193px;width:557px;height:234px;background:linear-gradient(90deg,#f4f4f4,#dcdcdc)}
.hero-week{position:absolute;left:20px;top:16px;font-family:"Yellowtail",cursive;color:var(--red);font-size:36px}
.hero-title{position:absolute;left:18px;top:48px;font-family:"Oswald",sans-serif;font-weight:300;font-size:60px;line-height:62px;color:#222}
.hero-sub{position:absolute;left:20px;top:112px;font-family:"Oswald",sans-serif;font-weight:300;font-size:26px;letter-spacing:7px;color:#555}
.hero-glasses{position:absolute;left:4px;top:155px;width:370px;height:75px;background:linear-gradient(90deg,#8a6a4a,#4a5040,#7a746c,#ddd)}
.hero-model{position:absolute;right:0;top:0;width:225px;height:234px;background:linear-gradient(110deg,#d6d0c8,#6a5040 45%,#2a2220)}

/* content */
.content{left:223px;top:427px;width:557px;height:693px;background:var(--white)}
.section-head{position:absolute;left:0;width:557px;height:30px;background:linear-gradient(#fff,#ececec);border-bottom:1px solid #ddd;font-weight:700;font-size:21px;padding:3px 16px}
.section-head.red{color:var(--red)}
.grid{position:absolute;left:16px;display:grid;grid-template-columns:repeat(4,127px);column-gap:9px}
.product{height:164px;position:relative}
.product .photo{height:108px;border:1px solid #e2e2e2;border-bottom:none;margin:0 2px}
.product .name{font-size:8.5px;font-weight:700;text-align:center;margin-top:6px}
.product .meta{display:flex;justify-content:space-between;padding:3px 8px 0 12px}
.product .price{color:var(--price);font-weight:700;font-size:14px}
.product .stars{color:var(--orange);font-size:9px;letter-spacing:-1px;line-height:18px}
.product .add{position:absolute;left:2px;right:0;bottom:0;height:18px;background:linear-gradient(#555,var(--btn) 50%,#000);color:var(--white);font-size:8.5px;font-weight:700;text-align:center;line-height:18px;border-radius:2px}

/* footer */
.footer{left:223px;top:1131px;width:557px;height:62px;background:linear-gradient(#5a5a5a,#333);color:var(--white);font-size:9px;border-radius:3px}
.footer .copy{position:absolute;left:26px;top:30px}
.footer .links{position:absolute;right:14px;top:30px}
</style>
</head>
<body>
<div class="page"></div>

<header>
  <div class="abs topbar"></div>
  <div class="abs brand"><span class="brand-mark"></span>Pennworths Top Finds</div>
  <nav class="abs topnav">Value of the Day &nbsp;|&nbsp; Local Ad &nbsp;|&nbsp; Store Finder &nbsp;|&nbsp; Registry &nbsp;|&nbsp;Gift Cards</nav>

  <div class="abs searchbar"></div>
  <div class="abs search-label">Search</div>
  <div class="abs select">All departments</div>
  <div class="abs keyword">Search keyword...</div>
  <div class="abs go">»</div>
  <div class="abs account">NewCustomer? <span class="hl">Sign in</span> | Help<br><span class="hl">My Cart</span> | My Accounts | My Lists</div>

  <div class="abs promo-black">BACK IN <b>BLACK FRIDAY</b><span class="preview">Preview Now ›</span></div>
  <div class="abs promo-bag">
    <div class="title">BAG GREAT SAVINGS</div>
    <div class="sub">Get Coupons + Learn More ›</div>
    <div class="goods" role="img" aria-label="Household product packages"></div>
  </div>
</header>

<aside>
  <div class="abs newbox">NEW TO THE WEBSITE<br><span>CLICK HERE</span></div>
  <div class="abs tabs"><div class="tab active">Catetories</div><div class="tab">Brands</div></div>
  <ul class="abs cats">
    <li>Electronics &amp; Office</li><li>Movies, Music &amp; Books</li><li>Home, Furniture &amp; Outdoor</li>
    <li>Apparel, Shoes &amp; Jewelery</li><li>Baby &amp; Kids</li><li>Toys &amp; Video Games</li>
    <li>Sports &amp; Fitness</li><li>Auto &amp; Home Improvements</li><li>Photo</li>
    <li>Crafts &amp; Party Supplies</li><li>Pharmacy, Health &amp; Beauty</li><li>Grocery &amp; Pets</li>
    <li>Toys &amp; Video Games</li><li>Sports &amp; Fitness</li><li>Auto &amp; Home Improvements</li>
    <li>Photo</li><li>Crafts &amp; Party Supplies</li><li>Pharmacy, Health &amp; Beauty</li>
  </ul>
  <div class="abs shipbox">SHIPPING ON ALL US <span class="w">ORDERS</span> <span class="w">OR</span><br><span class="b">EXPRESS DELIVERY</span></div>
  <div class="abs eurobox">FREE EURO DELIVERY<br>ON ORDER OVER<div class="amt"><small>$</small>150</div></div>
  <div class="abs social">
    <h4>Join our social network</h4>
    <div class="social-row"><span class="chip">Gather</span><span class="chip">Worklink</span><span class="chip">Tagbox</span><span class="chip">Murmur</span></div>
  </div>
  <div class="abs cards">
    <div class="card">Norvel</div><div class="card">Quorra</div><div class="card">Valta</div><div class="card">Coinlet</div>
  </div>
</aside>

<main>
  <section class="abs hero">
    <div class="hero-week">This Week's</div>
    <div class="hero-title">BUYERS' PICS</div>
    <div class="hero-sub">MEN EYEWARES</div>
    <div class="hero-glasses" role="img" aria-label="Three pairs of aviator sunglasses"></div>
    <div class="hero-model" role="img" aria-label="Man wearing dark sunglasses"></div>
  </section>

  <section class="abs content">
    <h2 class="section-head red" style="top:6px">FEATURED ITEMS</h2>
    <div class="grid" style="top:49px">
      <div class="product"><div class="photo" role="img" aria-label="Plaid shorts with sandals" style="background:linear-gradient(#fff,#d9d2cc 50%,#fff)"></div><div class="name">Ridgeway Shorts (Men)</div><div class="meta"><span class="price">$39.95</span><span class="stars">★★★★★</span></div><div class="add">Add to cart</div></div>
      <div class="product"><div class="photo" role="img" aria-label="Grey graphic tee" style="background:linear-gradient(#fff,#5a5a5a 50%,#fff)"></div><div class="name">Graphic Tees</div><div class="meta"><span class="price">$39.95</span><span class="stars">★★★★★</span></div><div class="add">Add to cart</div></div>
      <div class="product"><div class="photo" role="img" aria-label="Beach bag with sunglasses and sunscreen" style="background:linear-gradient(#fff,#f08a5a 50%,#fff)"></div><div class="name">Beach Bag Essentials</div><div class="meta"><span class="price">$39.95</span><span class="stars">★★★★★</span></div><div class="add">Add to cart</div></div>
      <div class="product"><div class="photo" role="img" aria-label="Boys striped tees multi pack" style="background:linear-gradient(#fff,#4aa060 50%,#fff)"></div><div class="name">Boys Multi Pack</div><div class="meta"><span class="price">$39.95</span><span class="stars">★★★★★</span></div><div class="add">Add to cart</div></div>
    </div>

    <h2 class="section-head" style="top:244px">NEW PRODUCTS</h2>
    <div class="grid" style="top:302px">
      <div class="product"><div class="photo" role="img" aria-label="Brown patterned cushions" style="background:linear-gradient(#fff,#6a4a34 50%,#fff)"></div><div class="name">Ridgeway Shorts (Men)</div><div class="meta"><span class="price">$39.95</span><span class="stars">★★★★★</span></div><div class="add">Add to cart</div></div>
      <div class="product"><div class="photo" role="img" aria-label="Pink girls graphic tee" style="background:linear-gradient(#fff,#e0408a 50%,#fff)"></div><div class="name">Graphic Tees</div><div class="meta"><span class="price">$39.95</span><span class="stars">★★★★★</span></div><div class="add">Add to cart</div></div>
      <div class="product"><div class="photo" role="img" aria-label="Boys striped tees" style="background:linear-gradient(#fff,#4aa060 50%,#fff)"></div><div class="name">Beach Bag Essentials</div><div class="meta"><span class="price">$39.95</span><span class="stars">★★★★★</span></div><div class="add">Add to cart</div></div>
      <div class="product"><div class="photo" role="img" aria-label="Beach bag with accessories" style="background:linear-gradient(#fff,#f08a5a 50%,#fff)"></div><div class="name">Boys Multi Pack</div><div class="meta"><span class="price">$39.95</span><span class="stars">★★★★★</span></div><div class="add">Add to cart</div></div>
    </div>
    <div class="grid" style="top:500px">
      <div class="product"><div class="photo" role="img" aria-label="Dark red polo shirt" style="background:linear-gradient(#fff,#8a1420 50%,#fff)"></div><div class="name">Ridgeway Shorts (Men)</div><div class="meta"><span class="price">$39.95</span><span class="stars">★★★★★</span></div><div class="add">Add to cart</div></div>
      <div class="product"><div class="photo" role="img" aria-label="Children's book cover" style="background:linear-gradient(#fff,#d8e040 50%,#fff)"></div><div class="name">Graphic Tees</div><div class="meta"><span class="price">$39.95</span><span class="stars">★★★★★</span></div><div class="add">Add to cart</div></div>
      <div class="product"><div class="photo" role="img" aria-label="Blue umbrella stroller" style="background:linear-gradient(#fff,#7aa8d0 50%,#fff)"></div><div class="name">Beach Bag Essentials</div><div class="meta"><span class="price">$39.95</span><span class="stars">★★★★★</span></div><div class="add">Add to cart</div></div>
      <div class="product"><div class="photo" role="img" aria-label="Black baby stroller" style="background:linear-gradient(#fff,#3a3a3a 50%,#fff)"></div><div class="name">Boys Multi Pack</div><div class="meta"><span class="price">$39.95</span><span class="stars">★★★★★</span></div><div class="add">Add to cart</div></div>
    </div>
  </section>
</main>

<footer class="abs footer">
  <span class="copy">All Rights Reserved 2011</span>
  <span class="links">Home / About Us / Privacy Policy / Contact Us</span>
</footer>
</body>
</html>
```